Business Card Design Project

We need business cards for the new company Market Helix based in Abu Dhabi, UAE, which provides IT retail solutions to businesses
Design should be done as a template, so we can add people when needed.
Please see attached details.
The brief is about 2 companies from our group. We need a business card only for Market Helix
Industry/Entity Type
Retail
Look and feel
Each slider illustrates characteristics of the customer's brand and the style your logo design should communicate.

```html
<!DOCTYPE html>
<html lang="en">
<head>
<meta charset="UTF-8">
<title>Market Helix – Business Card</title>
<link rel="stylesheet" href="https://fonts.googleapis.com/css2?family=Open+Sans:wght@600;700&display=swap">
<style>
  :root {
    --page-bg: #e7e5ea;
    --card-white: #f6f6f8;
    --card-shade: #ebebef;
    --brand-purple: #6a4ea4;
    --brand-purple-light: #7758b4;
    --brand-gold: #d6a92a;
    --text-on-purple: #ffffff;
  }
  * { box-sizing: border-box; margin: 0; padding: 0; }
  html, body {
    width: 1200px;
    height: 900px;
    overflow: hidden;
    background: var(--page-bg);
  }
  .canvas {
    position: relative;
    width: 1200px;
    height: 900px;
    display: flex;
    align-items: center;
    justify-content: center;
  }
  .business-card {
    position: relative;
    width: 1000px;
    height: 600px;
    background: linear-gradient(160deg, var(--card-white) 0%, var(--card-shade) 100%);
    box-shadow: 0 18px 40px rgba(40, 30, 60, 0.22);
    overflow: hidden;
  }
  .card-waves {
    position: absolute;
    inset: 0;
    width: 100%;
    height: 100%;
  }
  .wave-stripe { fill: var(--brand-purple-light); }
  .wave-base { fill: var(--brand-purple); }
  .brand-mark {
    position: absolute;
    left: 470px;
    top: 250px;
    display: flex;
    align-items: center;
    gap: 16px;
  }
  .brand-dot {
    width: 22px;
    height: 22px;
    border-radius: 50%;
    background: var(--brand-gold);
  }
  .brand-name {
    font-family: "Open Sans", Arial, sans-serif;
    font-weight: 700;
    font-size: 46px;
    letter-spacing: 0.5px;
    color: var(--brand-purple);
  }
  .website {
    position: absolute;
    left: 300px;
    top: 488px;
    font-family: "Open Sans", Arial, sans-serif;
    font-weight: 600;
    font-size: 28px;
    letter-spacing: 0.5px;
    color: var(--text-on-purple);
  }
</style>
</head>
<body>
  <main class="canvas">
    <section class="business-card" aria-label="Market Helix business card">
      <svg class="card-waves" viewBox="0 0 1000 600" preserveAspectRatio="none" aria-hidden="true">
        <path class="wave-stripe" d="M0,380 C250,335 560,395 1000,525 L1000,542 C560,418 260,368 0,405 Z"/>
        <path class="wave-base" d="M0,432 C260,395 560,450 1000,560 L1000,600 L0,600 Z"/>
      </svg>
      <div class="brand-mark">
        <span class="brand-dot"></span>
        <span class="brand-name">Market Helix</span>
      </div>
      <p class="website">www.mhxretail.ae</p>
    </section>
  </main>
</body>
</html>
```